Invitation Design Project

I need a customized graphic design for my wedding invitation.I want it to be non-traditional wedding invite. The design in mind is like a movie poster graphics while adopting 'the brighter days of the islands' font style and colors that create a light mood at the front page.Inside pages can be similar to movie posters with dark background similar to that of Ashen warden.Wedding related art/graphics can be integrated within the design.Wordings can be discussed later.

Industry/Entity Type

Graphic Design

Requirements
Must have
• Other must have features are our pictures as couple which will be sent .
Nice to have
• we would like to have the words

"our wedding.

more fun if you'll come!"

on the front cover.

```html
<!DOCTYPE html>
<html lang="en">
<head>
<meta charset="utf-8">
<title>Our Wedding – You Are Invited</title>
<link rel="stylesheet" href="https://fonts.googleapis.com/css2?family=Black+Ops+One&family=Russo+One&family=Varela+Round&display=swap">
<style>
  :root {
    --sky-centre: #22aee0;
    --sky-edge: #0a78a8;
    --ink: #111111;
    --tape-yellow: #f7e81c;
    --tape-green: #b8dc3c;
    --splash-orange: #f7941d;
    --splash-red: #ee3a43;
    --splash-magenta: #d62a8a;
    --splash-violet: #7a4ba8;
    --photo-warm: #c98a6a;
    --photo-dark: #3a3a3a;
    --photo-pink: #e94a9a;
    --white: #ffffff;
  }
  * { margin: 0; padding: 0; box-sizing: border-box; }
  html, body { width: 1200px; height: 938px; overflow: hidden; }
  body { background: var(--sky-edge); }

  .invitation {
    position: relative;
    width: 1200px;
    height: 938px;
    overflow: hidden;
    background: radial-gradient(ellipse 75% 80% at 55% 45%, var(--sky-centre) 0%, #1596cb 55%, var(--sky-edge) 100%);
  }
  .artwork { position: absolute; inset: 0; width: 1200px; height: 938px; }

  .tape-text {
    font-family: "Russo One", sans-serif;
    font-size: 17px;
    fill: var(--ink);
    letter-spacing: 0.5px;
  }

  .headline {
    position: absolute;
    left: 764px;
    top: 300px;
    transform: rotate(-9deg);
    transform-origin: left bottom;
    color: var(--ink);
  }
  .headline-our,
  .headline-wedding {
    font-family: "Russo One", sans-serif;
    line-height: 0.92;
    text-transform: uppercase;
    display: block;
  }
  .headline-our { font-size: 46px; }
  .headline-wedding { font-size: 60px; letter-spacing: 1px; }
  .headline-tagline {
    font-family: "Varela Round", sans-serif;
    font-size: 29px;
    display: block;
    margin-top: 2px;
    margin-left: 30px;
    letter-spacing: -0.3px;
  }

  .brand-mark {
    position: absolute;
    left: 770px;
    top: 190px;
    display: flex;
    align-items: center;
    gap: 10px;
    font-family: "Varela Round", sans-serif;
    font-size: 17px;
    color: var(--white);
  }
  .brand-dot {
    width: 16px; height: 16px; border-radius: 50%;
    background: var(--white);
  }

  .invite-stamp {
    position: absolute;
    left: 800px;
    top: 540px;
    transform: rotate(-12deg);
    transform-origin: left top;
    color: var(--ink);
    font-family: "Black Ops One", sans-serif;
  }
  .invite-stamp-lead { display: block; font-size: 33px; margin-left: 2px; }
  .invite-stamp-main {
    display: inline-block;
    font-size: 54px;
    line-height: 1;
    padding: 4px 14px 6px;
    border: 4px solid var(--ink);
    border-radius: 10px;
    margin-top: 2px;
    margin-left: 22px;
  }
</style>
</head>
<body>
<main class="invitation">
  <svg class="artwork" viewBox="0 0 1024 800" xmlns="http://www.w3.org/2000/svg">
    <defs>
      <radialGradient id="splash-fill" cx="0.45" cy="0.5" r="0.6">
        <stop offset="0" stop-color="var(--splash-red)"/>
        <stop offset="0.35" stop-color="var(--splash-orange)" stop-opacity="0.9"/>
        <stop offset="0.65" stop-color="var(--splash-magenta)" stop-opacity="0.6"/>
        <stop offset="1" stop-color="var(--splash-violet)" stop-opacity="0"/>
      </radialGradient>
      <linearGradient id="couple-fill" x1="0" y1="0" x2="1" y2="1">
        <stop offset="0" stop-color="var(--photo-warm)"/>
        <stop offset="0.45" stop-color="var(--photo-pink)"/>
        <stop offset="1" stop-color="var(--photo-dark)"/>
      </linearGradient>
    </defs>

    <!-- paint splash artwork -->
    <ellipse class="paint-splash" role="img" aria-label="Colourful paint splash artwork in orange, red, magenta and violet"
             cx="330" cy="330" rx="290" ry="300" fill="url(#splash-fill)"/>

    <!-- caution-style tapes -->
    <g class="tapes" transform="rotate(-13.1 0 573)">
      <rect class="tape tape-green" x="-60" y="561" width="1200" height="24" fill="var(--tape-green)"/>
      <text class="tape-text" x="-40" y="579">our Wedding ▫ our Wedding ▫ our Wedding ▫ our Wedding ▫ our Wedding ▫ our Wedding ▫ our Wedding ▫ our Wedding</text>
      <rect class="tape tape-yellow" x="-60" y="590" width="1200" height="24" fill="var(--tape-yellow)"/>
      <text class="tape-text" x="-20" y="608">our Wedding ▫ our Wedding ▫ our Wedding ▫ our Wedding ▫ our Wedding ▫ our Wedding ▫ our Wedding ▫ our Wedding</text>
    </g>

    <!-- couple photograph -->
    <rect class="couple-photo" role="img" aria-label="Photograph of the engaged couple embracing and smiling"
          x="318" y="170" width="398" height="630" rx="60" fill="url(#couple-fill)"/>
  </svg>

  <div class="brand-mark"><span class="brand-dot"></span>the brighter days of the islands</div>

  <h1 class="headline">
    <span class="headline-our">Our</span>
    <span class="headline-wedding">Wedding</span>
    <span class="headline-tagline">more fun.. if you will come</span>
  </h1>

  <p class="invite-stamp">
    <span class="invite-stamp-lead">YOU ARE</span>
    <span class="invite-stamp-main">INVITED</span>
  </p>
</main>
</body>
</html>
```